Tove & Lark Designs - Promotions flyer

I am a locally based Interior designer /stylist on Sydney's lower north shore. I would like to offer my services:
Full Professional Styling Services and Furniture Hire
Colour Consultation – Interior / exterior
Floor Coverings
Furniture selection and sourcing
Window Treatments
Wallpaper
Soft Furnishings
Upholstery
Renovations

I would like to offer a free consultation
Updates

Project Deadline Extended
Reason: I've been speaking with a designer and need her to make one more change. I have tried to message her twice, but have had no reply. Once she makes these changes I'm ready to sign off on the design. Thanks Harriet

Target Market(s)

30 - 60's middle to high income earners

Industry/Entity Type

Floor

Requirements
Must have
• one sided DL size
Use my logo
1 or 2 images of interior space or image of a lamp, cushion, lounge etc
The following contact details:
Mobile: 041 xxx xxxx
Website Address: www.tovelarkdesigns.example.au

```html
<!DOCTYPE html>
<html lang="en">
<head>
<meta charset="utf-8">
<title>Tove &amp; Lark Designs – Promotions Flyer</title>
<link rel="stylesheet" href="https://fonts.googleapis.com/css2?family=Arimo:ital,wght@0,400;1,400&display=swap">
<style>
  :root {
    --paper: #efefec;
    --brand-orange: #e2531f;
    --band-red: #e8461b;
    --ink: #3b3b3b;
    --ink-soft: #4a4a4a;
    --band-ink: #4a3a35;
  }
  * { margin: 0; padding: 0; box-sizing: border-box; }
  html, body { width: 1200px; height: 566px; overflow: hidden; }
  body {
    background: var(--paper);
    font-family: "Arimo", Arial, sans-serif;
    color: var(--ink);
  }
  .flyer {
    position: relative;
    width: 1200px;
    height: 566px;
    overflow: hidden;
    background: radial-gradient(ellipse at 50% 30%, #f5f5f3 0%, var(--paper) 70%);
  }
  .brand-name {
    position: absolute;
    top: 52px;
    left: 0;
    width: 1200px;
    text-align: center;
    font-size: 46px;
    font-weight: 400;
    color: var(--brand-orange);
    letter-spacing: 0.5px;
  }
  .intro {
    position: absolute;
    top: 214px;
    left: 32px;
    width: 566px;
    font-size: 14.4px;
    font-style: italic;
    line-height: 18.4px;
    text-align: justify;
    color: var(--ink);
  }
  .gallery { position: absolute; top: 378px; left: 28px; height: 140px; }
  .photo { position: absolute; top: 0; height: 140px; }
  .photo--kitchen {
    left: 0; width: 238px;
    background: linear-gradient(160deg, #9fb8c4 0%, #d9dfe0 45%, #8c6a52 100%);
  }
  .photo--bedroom {
    left: 242px; width: 94px;
    background: linear-gradient(180deg, #c9cdd0 0%, #e6e6e4 50%, #3d3a40 100%);
  }
  .photo--lounge {
    left: 340px; width: 232px;
    background: linear-gradient(170deg, #a9b7b9 0%, #eceeee 45%, #f7f7f7 70%, #5d5b58 100%);
  }
  .services {
    position: absolute;
    top: 214px;
    left: 640px;
    list-style: none;
    font-size: 20.5px;
    line-height: 27.5px;
    color: var(--ink);
  }
  .offer {
    position: absolute;
    top: 497px;
    left: 770px;
    font-size: 19px;
    color: var(--ink);
  }
  .contact-band {
    position: absolute;
    left: 0;
    top: 518px;
    width: 1200px;
    height: 48px;
    background: var(--band-red);
  }
  .website {
    position: absolute;
    left: 82px;
    top: 7px;
    font-size: 26px;
    color: var(--band-ink);
  }
  .postal, .phone {
    position: absolute;
    top: 14px;
    font-size: 14.4px;
    color: var(--band-ink);
  }
  .postal { left: 610px; }
  .phone { left: 916px; }
</style>
</head>
<body>
<main class="flyer">
  <header class="brand-name">Tove &amp; Lark Designs</header>

  <p class="intro">Tove &amp; Lark Designs prides itself in the ability to understand a clients brief and turn it into a reality. At the initial consult we will discuss your requirements and take time to understand your needs and sense of style. You will receive a written report outlining suggestions discussed in the consultation. The added benefits of using our services is that we are always happy to pass on trade discounts where possible to our clients.</p>

  <div class="gallery">
    <div class="photo photo--kitchen" role="img" aria-label="Photo of a bright kitchen and dining area with timber chairs and flowers"></div>
    <div class="photo photo--bedroom" role="img" aria-label="Photo of a styled bedroom with a lamp and dark bedding"></div>
    <div class="photo photo--lounge" role="img" aria-label="Photo of a white open-plan lounge room with flowers on a coffee table"></div>
  </div>

  <ul class="services">
    <li>Full Professional Styling Services and Furniture Hire</li>
    <li>Colour Consultation – Interior / exterior</li>
    <li>Floor Coverings</li>
    <li>Furniture selection and sourcing</li>
    <li>Window Treatments</li>
    <li>Wallpaper</li>
    <li>Soft Furnishings</li>
    <li>Upholstery</li>
    <li>Renovations</li>
  </ul>

  <p class="offer">FREE CONSULTATION</p>

  <footer class="contact-band">
    <span class="website">www.tovelarkdesigns.example.au</span>
    <span class="postal">PO Box 731 Harbour Point NSW 2090</span>
    <span class="phone">Telephone: +61 (0)41x xxx xxx</span>
  </footer>
</main>
</body>
</html>
```